Creative Photography Business Card

Looking for a unique, creative, elegant, sophisticated and professional business card for my photography business.

I specialise in children, families, modelling, weddings and special event photography

Things to include:
Logo - will attach
Email: hello@mirenholtstudio.com.au
web:www.mirenholtstudio.com.au
Ph: 0438 561 204

I will also upload some of my work that you may like to use.

Please be creative and unique in your designs.

Reason: Currently away for work...finding it hard to give feedback in time for the deadline - sorry.

```html
<!DOCTYPE html>
<html lang="en">
<head>
<meta charset="utf-8">
<title>Miren Holt Studio – Business Card</title>
<link rel="stylesheet" href="https://fonts.googleapis.com/css2?family=Montserrat:wght@300;400;600;700&family=Open+Sans:wght@400&display=swap">
<style>
  :root {
    --page-bg: #eceef1;
    --card-white: #ffffff;
    --brand-navy: #1f4f86;
    --brand-blue: #2a6db0;
    --brand-sky: #6aa5d8;
    --text-dark: #333a42;
    --grad-light: #0aa0dc;
    --grad-mid: #1b78b8;
    --grad-deep: #1b4a86;
    --line-white: rgba(255,255,255,0.85);
  }
  * { box-sizing: border-box; margin: 0; padding: 0; }
  html, body { width: 1200px; height: 900px; overflow: hidden; }
  body {
    background: var(--page-bg);
    font-family: "Open Sans", Arial, sans-serif;
    display: flex;
    flex-direction: column;
    align-items: center;
    justify-content: center;
    gap: 56px;
  }
  .card {
    position: relative;
    width: 600px;
    height: 343px;
    border-radius: 4px;
    overflow: hidden;
    box-shadow: 0 6px 18px rgba(0,0,0,0.12);
  }

  /* Front */
  .card-front { background: var(--card-white); }
  .corner {
    position: absolute;
    width: 26px;
    height: 26px;
    border-color: var(--brand-navy);
    border-style: solid;
    border-width: 0;
  }
  .corner-top-left { top: 24px; left: 24px; border-top-width: 2px; border-left-width: 2px; }
  .corner-bottom-left { bottom: 84px; left: 24px; border-bottom-width: 2px; border-left-width: 2px; }
  .corner-mid-right { bottom: 110px; right: 24px; border-top-width: 2px; border-right-width: 2px; }
  .corner-bottom-right { bottom: 24px; right: 24px; border-bottom-width: 2px; border-right-width: 2px; }

  .identity {
    position: absolute;
    top: 62px;
    left: 250px;
    font-family: "Montserrat", Arial, sans-serif;
  }
  .identity-name {
    font-size: 25px;
    font-weight: 300;
    letter-spacing: 1px;
    color: var(--text-dark);
  }
  .identity-name strong { font-weight: 700; color: var(--brand-navy); }
  .identity-role {
    font-size: 17px;
    font-weight: 300;
    color: var(--brand-sky);
    margin-top: 2px;
  }
  .contact-list {
    position: absolute;
    top: 142px;
    left: 226px;
    list-style: none;
  }
  .contact-item {
    display: flex;
    align-items: center;
    gap: 14px;
    font-size: 14px;
    color: var(--text-dark);
    height: 27px;
  }
  .contact-icon { width: 16px; height: 16px; fill: var(--brand-navy); }
  .specialities {
    position: absolute;
    left: 58px;
    bottom: 46px;
    font-family: "Montserrat", Arial, sans-serif;
    font-weight: 600;
    font-size: 14.5px;
    letter-spacing: 0.4px;
    text-transform: uppercase;
    color: var(--brand-blue);
  }

  /* Back */
  .card-back { background: linear-gradient(125deg, var(--grad-light) 0%, var(--grad-mid) 50%, var(--grad-deep) 100%); }
  .back-geometry { position: absolute; inset: 0; }
  .logo-name {
    position: absolute;
    top: 68px;
    left: 200px;
    width: 150px;
    display: flex;
    flex-direction: column;
    align-items: center;
    gap: 8px;
    font-family: "Montserrat", Arial, sans-serif;
    font-weight: 600;
    font-size: 20px;
    color: var(--brand-navy);
    text-align: center;
    line-height: 1.1;
  }
  .logo-dot { width: 12px; height: 12px; border-radius: 50%; background: var(--brand-navy); }
  .back-signature {
    position: absolute;
    right: 70px;
    bottom: 48px;
    font-family: "Montserrat", Arial, sans-serif;
    font-weight: 400;
    color: var(--card-white);
    text-align: center;
    font-size: 20px;
    letter-spacing: 1px;
    line-height: 1.2;
  }
  .back-signature span { display: block; font-size: 11px; letter-spacing: 3px; }
</style>
</head>
<body>
  <section class="card card-front" aria-label="Business card front">
    <span class="corner corner-top-left"></span>
    <span class="corner corner-bottom-left"></span>
    <span class="corner corner-mid-right"></span>
    <span class="corner corner-bottom-right"></span>

    <div class="identity">
      <h1 class="identity-name"><strong>MIREN</strong> HOLT</h1>
      <p class="identity-role">Photographer</p>
    </div>

    <ul class="contact-list">
      <li class="contact-item">
        <svg class="contact-icon" viewBox="0 0 16 16" aria-hidden="true"><path d="M1 3h14v10H1z M2 4l6 5 6-5" fill="none" stroke="#1f4f86" stroke-width="1.6"/></svg>
        hello@mirenholtstudio.com.au
      </li>
      <li class="contact-item">
        <svg class="contact-icon" viewBox="0 0 16 16" aria-hidden="true"><g fill="none" stroke="#1f4f86" stroke-width="1.3"><circle cx="8" cy="8" r="6.5"/><ellipse cx="8" cy="8" rx="3" ry="6.5"/><path d="M1.5 8h13M2.5 4.5h11M2.5 11.5h11"/></g></svg>
        www.mirenholtstudio.com.au
      </li>
      <li class="contact-item">
        <svg class="contact-icon" viewBox="0 0 16 16" aria-hidden="true"><path d="M4 1.5l2.5 3-1.5 1.8c.8 1.8 2.2 3.2 4 4l1.8-1.5 3 2.5-1.5 2.5C7 13.5 2.5 9 1.5 3z"/></svg>
        0438 561 204
      </li>
    </ul>

    <p class="specialities">Children, Families, Modelling Weddings &amp; Special Event</p>
  </section>

  <section class="card card-back" aria-label="Business card back">
    <svg class="back-geometry" viewBox="0 0 600 343" aria-hidden="true">
      <polygon points="190,22 350,22 400,95 350,168 190,168 150,95" fill="#ffffff"/>
      <g stroke="rgba(255,255,255,0.85)" stroke-width="1.2" fill="none">
        <line x1="60" y1="0" x2="150" y2="95"/>
        <line x1="0" y1="150" x2="150" y2="95"/>
        <line x1="400" y1="95" x2="600" y2="20"/>
        <line x1="400" y1="95" x2="270" y2="343"/>
        <line x1="350" y1="168" x2="600" y2="343"/>
        <line x1="380" y1="0" x2="350" y2="22"/>
      </g>
    </svg>
    <div class="logo-name">
      <span class="logo-dot"></span>
      Miren Holt Studio
    </div>
    <p class="back-signature">Miren Holt<span>STUDIO</span></p>
  </section>
</body>
</html>
```